Silent Disco and Photo Booth Magazine Advertisements

We have two one-page advertisement placements in a magazine that is being distributed to thousands of people at a large Christian camp. We are targeting all the folks reading the ad, but especially want this catered to Youth Pastors, who are the ones who would make the buying decision on renting equipment from us. They need to have the exact same feel and vibe, hence being made together here.

We want one of these full-page advertisements to feature our Silent Disco Headsets, and the other to be focused on our Photo Booths. Our company rents and ships event equipment nationally as our primary service, and we want to feature that as the focus.

We are a fun company, provide fun entertainment equipment services, and take a 100% satisfaction approach to our customer service. We have a long-standing reputation for providing equipment that will be a guaranteed successful event and always arrive on time. It's easy, fun, and a fair value.

Attached are two mock-ups of some ideas we have around it. Some content options are below:

***Silent Disco Rentals***
Rentals starting at $5 per person (plus the cost of shipping)
Easy to setup
Works well for prayer and for silent disco fun
Guarantee to get everyone out for a fun time
Nation's biggest silent disco provider
50 or 5,000 we got you covered
Go to quietgroovehire.com/experiences/church/ to find our youth pastor event guide

**Photo booth**
Shippability (national)
Portability (very portable)
Setup in 5 minutes
Social fun aspect
Social sharing aspect (Lumigram/Circlebook)
Full branding: Use for contests, promotions, special sponsorships
KELNA special starting at $679 (crossed out $479) for 2022
Save $200 off of every order

PLEASE USE THESE COLORS:
Colors:
Pink- HEX #CC008F
HEX # 690065
Black- HEX #000000

Font:
Font- Montserrat (Primary)
Roboto (Secondary)

Target Market(s)

Youth Pastors, Pastors, Church Event Managers, Church Activity Directors 18-40 years old

Font styles to use
Other font styles liked:
• Font- Montserrat (Primary) Roboto (Secondary) (Pink- HEX #CC008F HEX # 690065 Black- HEX #000000)

Colors

Designer to choose colors to be used in the design.

Requirements
Must have
• Crisp, clear, call to action, explanation of offerings, great theme. Font- Montserrat (Primary) Roboto (Secondary) Pink- HEX #CC008F HEX # 690065 Black- HEX #000000

```html
<!DOCTYPE html>
<html lang="en">
<head>
<meta charset="utf-8">
<title>Photo Booth Rental Advertisement</title>
<link rel="stylesheet" href="https://fonts.googleapis.com/css2?family=Montserrat:wght@200;300;500;700;800&display=swap">
<style>
  :root {
    --pink: #CC008F;
    --plum: #690065;
    --black: #000000;
    --ink: #050608;
    --paper: #F2F2F2;
    --white: #FFFFFF;
  }
  * { margin: 0; padding: 0; box-sizing: border-box; }
  html, body { width: 848px; height: 1200px; overflow: hidden; background: var(--ink); }
  .ad {
    position: relative;
    width: 848px;
    height: 1200px;
    overflow: hidden;
    background: var(--ink);
    font-family: "Montserrat", sans-serif;
    color: var(--white);
  }
  .ad__top-band {
    position: absolute; left: 0; top: 0;
    width: 848px; height: 383px;
    background: var(--paper);
  }
  .ad__title {
    position: absolute;
    left: 48px; top: 700px;
    transform-origin: 0 0;
    transform: rotate(-90deg);
    white-space: nowrap;
    font-size: 88px;
    line-height: 1;
    letter-spacing: 0;
    z-index: 2;
  }
  .ad__title-light { font-weight: 200; color: var(--white); }
  .ad__title-bold { font-weight: 800; color: var(--plum); letter-spacing: -1px; }
  .ad__hero {
    position: absolute;
    left: 176px; top: 44px;
    width: 627px; height: 470px;
    background:
      radial-gradient(ellipse at 30% 55%, rgba(230,60,160,0.55), transparent 45%),
      radial-gradient(ellipse at 55% 40%, rgba(90,220,170,0.55), transparent 50%),
      radial-gradient(ellipse at 80% 25%, rgba(60,140,255,0.6), transparent 55%),
      linear-gradient(180deg, #0c3a6a 0%, #184e86 45%, #0a1a2c 78%, #04070c 100%);
  }
  .ad__booth {
    position: absolute;
    left: 598px; top: 490px;
    width: 150px; height: 480px;
    border-radius: 75px 75px 4px 4px;
    background: linear-gradient(180deg, #e9e9ea 0%, #bdbdc2 22%, #1a1a1c 32%, #0d0d0f 100%);
  }
  .features {
    position: absolute;
    left: 176px; top: 568px;
    list-style: none;
    width: 345px;
  }
  .features__item {
    position: relative;
    padding-left: 28px;
    font-size: 17px;
    font-weight: 500;
    line-height: 24px;
    margin-bottom: 25px;
  }
  .features__item::before {
    content: "";
    position: absolute;
    left: 0; top: 7px;
    width: 10px; height: 10px;
    border-radius: 50%;
    background: var(--pink);
  }
  .brand {
    position: absolute;
    left: 58px; top: 1060px;
    display: flex; align-items: center; gap: 10px;
    font-weight: 800;
    font-size: 22px;
    line-height: 1.05;
    color: var(--white);
    letter-spacing: 0.5px;
  }
  .brand__dot {
    width: 18px; height: 18px;
    border-radius: 50%;
    background: var(--white);
    flex: none;
  }
  .offer {
    position: absolute;
    left: 296px; top: 1002px;
    font-weight: 300;
    font-size: 73px;
    line-height: 78px;
    color: var(--white);
    white-space: nowrap;
  }
  .offer__amount { font-weight: 700; color: var(--pink); }
</style>
</head>
<body>
  <main class="ad">
    <div class="ad__top-band"></div>

    <div class="ad__hero" role="img" aria-label="Concert crowd under colourful stage lights and falling confetti"></div>

    <h1 class="ad__title"><span class="ad__title-light">PHOTO</span><span class="ad__title-bold">BOOTH</span></h1>

    <ul class="features">
      <li class="features__item">Shippability (national)</li>
      <li class="features__item">Portability (very portable)</li>
      <li class="features__item">Setup in 5 minutes</li>
      <li class="features__item">Social fun aspect</li>
      <li class="features__item">Full branding: Use for contests, promotions, special sponsorships</li>
      <li class="features__item">Social sharing aspect (Lumigram/Circlebook)</li>
      <li class="features__item">KELNA special starting at $679 (crossed out $479) for 2022</li>
    </ul>

    <div class="ad__booth" role="img" aria-label="Selfie station photo booth with ring light on a black stand"></div>

    <div class="brand">
      <span class="brand__dot"></span>
      <span>QUIET GROOVE<br>HIRE</span>
    </div>

    <p class="offer">Save <span class="offer__amount">$200 off</span><br>of every order</p>
  </main>
</body>
</html>
```